依頼概要
■依頼の目的
マタニティさん向けの本の表紙デザインをお願いします。

■本の内容
胎内記憶による、しあわせな出産と育児のためのマタニティライフの過ごし方

第一章 胎内記憶を知ってマタニティライフを過ごしましょう
第二章 おなかの赤ちゃんとコミュニケーション
第三章 しあわせなお産をしよう
第四章 出産後のことを考えておこう
第五章 0歳育児が大切なことは意外と知られていない
第六章 夫婦で妊娠出産を楽しむ~産後うつを防ぐ~

差し支えなければですが、「0歳児についてわかるサブキャッチ」を表紙にデザインしたいのでよろしくお願いします。

■デザイン要望
柔らかい雰囲気の若いママ向けのおしゃれな感じが望ましいです。

■著者の記載

全国育み言葉研究会認定講師
マタニティライフしあわせアドバイザー
北浦ミレーユ詩織

※どこかに
「胎内記憶の世界的第一人者
森下晃先生 推薦」を入れてほしいです。

その他 ご不明な点がございましたらお気軽にご質問下さい。
よろしくお願いいたします。
書き損じておりました。
電子書籍(Pagora)での出版になります。

画像サイズは
表紙ファイルの理想的な寸法は2560×1600ピクセルです。
画像の寸法は1000×625ピクセル以上であることが必要です。

次点、次次点のかたへの参加報酬を設定いたしました。
皆様の自由な発想のデザインを楽しみにしております。

その他、必要な情報がありましたらお問い合わせください。
ランサーのみなさま、たくさんおご提案ありがとうございました。
どれも秀逸で感動しております。
2月末までに決定させていただきたいと思います。
よろしくお願いいたします。
■ 選んだ理由

どれもかわいいデザインで迷いましたが、
美しい写真でクオリティが高いこと、一目でマタニティの本であるとわかること、
「お産が楽になる」という言葉を大きく書いてくださっているのを選ぶようにとアドバイスされました。

■ 提案者全員のお礼・コメント

自分ではとうてい思いつかないような、かわいくてわかりやすいデザインを考えてくださり、感動しました。原稿を読んで下さり、内容も考慮して下さって感謝の気持ちで一杯です。
本当に迷いました。今回はご縁がなかったかたも、すばらしいものばかりでした。ありがとうございました!!

```html
<!DOCTYPE html>
<html lang="ja">
<head>
<meta charset="utf-8">
<title>お産が楽になる胎内記憶の秘密</title>
<link rel="stylesheet" href="https://fonts.googleapis.com/css2?family=M+PLUS+Rounded+1c:wght@500;700;800;900&family=Kosugi+Maru&display=swap">
<style>
  :root{
    --paper:#fdf7f5;
    --pink:#e0708a;
    --pink-deep:#d0506f;
    --ink:#3b2a2a;
    --brown:#5a3a2c;
    --bubble:#e9d3b2;
    --bubble-edge:#d8bb92;
    --band:#f1e4d4;
  }
  *{margin:0;padding:0;box-sizing:border-box}
  html,body{width:750px;height:1200px;overflow:hidden;background:var(--paper)}
  .cover{position:relative;width:750px;height:1200px;overflow:hidden;
    background:radial-gradient(circle at 20% 10%,#fff 0,var(--paper) 60%);
    font-family:"M PLUS Rounded 1c","Kosugi Maru",sans-serif;color:var(--ink)}
  .endorse{position:absolute;left:22px;top:20px;color:var(--pink-deep);font-weight:800}
  .endorse .role{font-size:22px;display:block;line-height:1.2}
  .endorse .line{font-size:30px;line-height:1.3}
  .endorse .name{font-size:46px;font-weight:900}
  .gift{position:absolute;left:478px;top:72px;width:54px;height:50px;border-radius:8px;
    background:linear-gradient(#f48aa0,#e45c78)}
  .present{position:absolute;right:10px;top:30px;width:200px;text-align:center;
    color:var(--pink-deep);font-size:18px;font-weight:700;line-height:1.3}
  .present .tag{display:inline-block;background:var(--pink);color:#fff;border-radius:12px;padding:2px 12px;margin-bottom:4px;font-size:20px}
  .lead{position:absolute;left:0;right:0;top:108px;text-align:center;font-size:66px;font-weight:900;letter-spacing:4px;color:var(--ink);white-space:nowrap}
  .title-band{position:absolute;left:70px;top:186px;width:650px;height:110px;border-radius:55px;
    background:var(--pink);color:#fff;font-size:100px;font-weight:900;text-align:center;line-height:110px;letter-spacing:12px;white-space:nowrap}
  .title-tail{position:absolute;left:18px;top:290px;font-size:56px;font-weight:900;color:var(--pink-deep);white-space:nowrap}
  .belly{position:absolute;left:0;top:370px;width:290px;height:630px;border-radius:0 150px 150px 0;
    background:radial-gradient(ellipse at 40% 55%,#6b5a58 0,#2d2222 70%)}
  .bubble{position:absolute;left:250px;top:375px;width:480px;height:340px}
  .bubble-text{position:absolute;left:280px;top:440px;width:420px;transform:rotate(-14deg);transform-origin:center;
    text-align:center;color:var(--brown);font-weight:800;white-space:nowrap;line-height:1.2}
  .bubble-text .a{font-size:54px;display:block}
  .bubble-text .b{font-size:28px;display:block}
  .bubble-text .c{font-size:38px;display:block}
  .bubble-text .d{font-size:22px;display:block;margin-top:4px}
  .toy{position:absolute;border-radius:50%}
  .toy.bunny{left:375px;top:302px;width:52px;height:70px;background:#f3dce3}
  .toy.balloon{left:455px;top:300px;width:48px;height:66px;background:#f4a9a0}
  .toy.bear{left:650px;top:360px;width:86px;height:92px;background:#c9996a}
  .toy.ball{left:335px;top:795px;width:42px;height:42px;background:#f4d3a0}
  .toy.train{left:237px;top:870px;width:188px;height:110px;border-radius:14px;background:linear-gradient(90deg,#e9a36b,#9ac3d6,#e37c7c)}
  .couple{position:absolute;left:412px;top:752px;width:338px;height:340px;
    background:linear-gradient(180deg,#eef1f2,#d9dfe1);border-radius:6px 0 0 0}
  .sub{position:absolute;left:18px;top:1000px;font-size:34px;font-weight:900;color:var(--ink);letter-spacing:1px;white-space:nowrap}
  .creds{position:absolute;left:18px;top:1046px;font-size:19px;font-weight:700;line-height:1.3;color:var(--ink);font-family:"Kosugi Maru",sans-serif;white-space:nowrap}
  .author-band{position:absolute;left:0;top:1102px;width:750px;height:98px;background:var(--band)}
  .author{position:absolute;left:22px;top:1112px;font-size:60px;font-weight:900;color:var(--brown);letter-spacing:2px;white-space:nowrap}
</style>
</head>
<body>
<main class="cover">
  <p class="endorse"><span class="role">胎内記憶の世界的第一人者</span><span class="line"><span class="name">森下晃</span> 先生 推薦!</span></p>
  <div class="gift" role="img" aria-label="リボン付きのプレゼント箱のイラスト"></div>
  <p class="present"><span class="tag">タイプ別診断</span><br>おなかの赤ちゃんとの<br>コミュニケーションの<br>極め方を読者プレゼント♥</p>

  <h1>
    <span class="lead">お産が楽になる</span>
    <span class="title-band">胎内記憶</span>
    <span class="title-tail">の秘密</span>
  </h1>

  <div class="belly" role="img" aria-label="妊婦のおなかのシルエット写真と胎児のイラスト"></div>

  <svg class="bubble" viewBox="0 0 480 340" aria-hidden="true">
    <path d="M245 10 C390 10 472 80 472 165 C472 250 385 315 245 315 C205 315 172 308 145 298 L55 334 L92 276 C40 246 10 208 10 165 C10 80 100 10 245 10Z" fill="var(--bubble)" stroke="var(--bubble-edge)" stroke-width="3"/>
  </svg>
  <p class="bubble-text"><span class="a">夫婦で学ぶ</span><span class="b">おなかの赤ちゃんとの</span><span class="c">コミュニケーション</span><span class="d">早く会いたいよ~!</span></p>

  <div class="toy bunny" role="img" aria-label="うさぎのぬいぐるみのイラスト"></div>
  <div class="toy balloon" role="img" aria-label="風船のイラスト"></div>
  <div class="toy bear" role="img" aria-label="くまのぬいぐるみのイラスト"></div>
  <div class="toy ball" role="img" aria-label="ボールのイラスト"></div>
  <div class="toy train" role="img" aria-label="おもちゃの汽車のイラスト"></div>

  <div class="couple" role="img" aria-label="並んで立つ夫婦の写真"></div>

  <p class="sub">0歳児についてわかる</p>
  <p class="creds">全国育み言葉研究会認定講師<br>マタニティライフしあわせアドバイザー</p>
  <div class="author-band"></div>
  <p class="author">北浦ミレーユ詩織</p>
</main>
</body>
</html>
```